Corporate Breakfast Flyer - Breakfast Talk (One Page)

Create a flyer with below using your own selection of content and images from the below. You do not have to use all images I have left them all there for your choice. Please use blue type colors like in our logo. Should be a corporate and professional feel to it.

Venue: Carrowby Links Club 37 Wexley Rd, Carrowby NSW 2163
Date: Thursday the 22nd of September 2016
7.30am: Breakfast and networking
8.00am: Darren Voss speaking – Leadership and Motivation
9.00am: Business Card draw and finish

• Mini croissants on arrival – Ham & cheese, tomato & cheese, plain
• Toast station – assorted sliced breads & spreads
• Banana bread slice with honey ricotta
• Chicken & herb chipolata
• Marinated lamb chops
• Creamy scrambled eggs with chives
• Mushroom & cherry tomato kebabs
• Hash browns
• Assorted fruit cocktails with yoghurt & granola, juice station
• Tea and coffee station included
Topic: Leadership and Motivation
Speaker profile (Darren Voss):
Darren Voss is a four-time Meridian athlete, winning basketball player, coach, entrepreneur, motivational speaker, brand ambassador - and one of Australia's most recognized personalities and sporting figures.
He was the first-ever Australian player to be signed to the PCL from the TBF and he also captained the Harbour Falcons to their first-ever title, helping to raise the profile of basketball around Australia. He has represented Australia at four Meridian Games and played professionally for more than 20 years in Australia, Europe and the PCL. In February 2012 he was appointed Head Coach of the Harbour Falcons.
Following his retirement from playing, Darren earned a reputation as a successful entrepreneur and businessman. He built up a successful business in fast food franchising with more than 30 stores across six different brands which, at its peak in 2010, employed over 350 people. After his company was severely affected by the collapse of an QMR listed company in which he had purchased a 10-year contract, Darren had to start all over again.
Darren has also held hosting, commentary and columnist roles with UVT, Channel Pulse, Crest Network and Vista Sports.

Target Market(s)

Finance leaders, Finance Directors, Controllers and CFO's

Font styles to use
Serif
Sans Serif

Colors
33a6d7
0592cd
0355a3
3276b5
85abd2
85cae6

Requirements
Must have
• Must be one page A4 will be sent electronically
Nice to have
• Any other images you feel may be pertinant, I have attached lots of images for you to use for this project please do not use to many. I have attached more so you have more selection
Should not have
• All Images

```html
<!DOCTYPE html>
<html lang="en">
<head>
<meta charset="utf-8">
<title>Breakfast Seminar – Darren Voss</title>
<link href="https://fonts.googleapis.com/css2?family=Mulish:ital,wght@0,400;0,600;1,400&family=Roboto+Condensed:wght@700&display=swap" rel="stylesheet">
<style>
  :root{
    --navy:#0c4f8f;
    --royal:#0a6cbd;
    --menu-blue:#2f88d0;
    --slate:#7b8d9c;
    --slate-dark:#6f8191;
    --ink:#3a3f45;
    --brand-grey:#4a5158;
    --heading-blue:#1f5fa8;
    --yellow:#f4e94a;
    --white:#ffffff;
    --portrait:#5b4a44;
  }
  *{box-sizing:border-box;margin:0;padding:0}
  html,body{width:848px;height:1200px;overflow:hidden;background:var(--white)}
  body{font-family:"Mulish",Arial,sans-serif;color:var(--ink)}
  .flyer{position:relative;width:848px;height:1200px;overflow:hidden}
  .block{position:absolute}

  /* brand header */
  .brand{left:0;top:0;width:477px;height:230px;background:var(--white)}
  .brand-name{position:absolute;left:128px;top:70px;font-size:47px;font-weight:600;
    color:var(--brand-grey);letter-spacing:-.5px;line-height:1.1}
  .seminar-title{position:absolute;left:142px;top:152px;font-family:"Roboto Condensed",Arial,sans-serif;
    font-size:33px;font-weight:700;letter-spacing:-.3px}
  .seminar-title .accent{color:var(--royal)}
  .seminar-title .dark{color:#3a4450}

  /* date & venue */
  .details{left:477px;top:0;width:371px;height:230px;background:var(--navy);color:var(--white);text-align:center}
  .label{color:var(--yellow);font-size:23px;font-weight:600}
  .details .label.date{margin-top:50px}
  .details .value{font-size:20px;margin-top:3px}
  .details .label.venue{margin-top:14px}
  .details .venue-name{font-size:22px}
  .details .address{font-size:16.5px;margin-top:2px}

  /* speaker band */
  .speaker{left:0;top:230px;width:477px;height:157px;background:var(--royal);color:var(--white);text-align:center}
  .speaker .kicker{font-size:24px;margin-top:27px;letter-spacing:.5px}
  .speaker .name{font-size:32px;color:var(--yellow);margin-top:4px;letter-spacing:.5px}
  .speaker .topic{font-size:26px;font-style:italic;margin-top:12px}

  /* schedule */
  .schedule{left:477px;top:230px;width:371px;height:157px;background:var(--slate);color:var(--white);
    font-size:17.5px;padding:26px 0 0 26px}
  .schedule li{list-style:none;display:flex;margin-bottom:9px;line-height:1.25}
  .schedule .time{width:78px;flex:none}

  /* imagery */
  .portrait{left:0;top:387px;width:477px;height:455px;
    background:radial-gradient(ellipse at 42% 48%,#d9b9a3 0%,#b48a73 28%,var(--portrait) 55%,#2b2422 100%)}
  .venue-photo{left:477px;top:387px;width:371px;height:101px;
    background:linear-gradient(180deg,#0f1a2b 0%,#26364c 45%,#6d5a3f 70%,#2b3a2e 100%)}

  /* menu */
  .menu{left:477px;top:488px;width:371px;height:354px;background:var(--menu-blue);color:var(--white)}
  .menu h2{font-weight:400;color:var(--yellow);font-size:22px;text-align:center;margin-top:12px}
  .menu ul{list-style:none;padding:6px 14px 0 18px}
  .menu li{position:relative;padding-left:24px;font-size:16.2px;line-height:1.41}
  .menu li::before{content:"";position:absolute;left:2px;top:8px;width:6px;height:6px;background:var(--white);transform:rotate(45deg)}

  /* divider bands */
  .band-slate{left:0;top:842px;width:848px;height:14px;background:var(--slate-dark)}
  .band-blue{left:0;top:856px;width:848px;height:18px;background:var(--royal)}

  /* profile */
  .profile{left:0;top:874px;width:848px;height:231px;padding:5px 40px 0 42px}
  .profile h3{font-weight:400;color:var(--heading-blue);font-size:18px;margin-bottom:9px;letter-spacing:.2px}
  .profile p{font-size:13.3px;line-height:1.36;margin-bottom:8px;color:#444;letter-spacing:.2px}

  /* footer */
  .rsvp{left:0;top:1105px;width:422px;height:95px;background:var(--navy);color:var(--yellow);
    font-size:31px;display:flex;align-items:center;padding-left:84px}
  .phone{left:422px;top:1105px;width:426px;height:95px;background:var(--slate);color:var(--yellow);
    font-size:31px;display:flex;align-items:center;padding-left:82px;gap:16px;letter-spacing:.5px}
  .phone svg{width:26px;height:34px;flex:none}
</style>
</head>
<body>
<main class="flyer">

  <header class="block brand">
    <div class="brand-name">Kellan Marsh</div>
    <div class="seminar-title"><span class="accent">BREAKFAST</span> <span class="dark">SEMINAR</span></div>
  </header>

  <section class="block details">
    <div class="label date">DATE</div>
    <div class="value">Thursday, 22nd September, 2016</div>
    <div class="label venue">VENUE</div>
    <div class="venue-name">Carrowby Links Club</div>
    <div class="address">37 Wexley Rd, Carrowby NSW 2163</div>
  </section>

  <section class="block speaker">
    <div class="kicker">GUEST SPEAKER</div>
    <div class="name">DARREN VOSS</div>
    <div class="topic">“Leadership and Motivation”</div>
  </section>

  <ul class="block schedule">
    <li><span class="time">7.30 am</span><span>Breakfast and networking</span></li>
    <li><span class="time">8.00 am</span><span>Darren Voss speaking –<br>Leadership &amp; Motivation</span></li>
    <li><span class="time">9.00 am</span><span>Business Card draw &amp; finish</span></li>
  </ul>

  <div class="block portrait" role="img" aria-label="Portrait photograph of guest speaker Darren Voss"></div>
  <div class="block venue-photo" role="img" aria-label="Night-time photograph of the Carrowby Links Club clubhouse"></div>

  <section class="block menu">
    <h2>MENU</h2>
    <ul>
      <li>Mini croissants on arrival – Ham &amp; cheese, tomato &amp; cheese, plain</li>
      <li>Toast station – assorted sliced breads &amp; spreads</li>
      <li>Banana bread slice with honey ricotta</li>
      <li>Chicken &amp; herb chipolata</li>
      <li>Marinated lamb chops</li>
      <li>Creamy scrambled eggs with chives</li>
      <li>Mushroom &amp; cherry tomato kebabs</li>
      <li>Hash browns</li>
      <li>Assorted fruit cocktails with yoghurt &amp; granola, juice station</li>
      <li>Tea and coffee station included</li>
    </ul>
  </section>

  <div class="block band-slate"></div>
  <div class="block band-blue"></div>

  <section class="block profile">
    <h3>SPEAKER PROFILE - DARREN VOSS</h3>
    <p>Darren Voss is a four-time Meridian athlete, winning basketball player, coach, entrepreneur, motivational speaker, brand ambassador - and one of Australia's most recognized personalities and sporting figures.</p>
    <p>He has represented Australia at four Meridian Games and played professionally for more than 20 years in Australia, Europe and the PCL. In February 2012 he was appointed Head Coach of the Harbour Falcons. Following his retirement from playing, Darren earned a reputation as a successful entrepreneur and businessman.</p>
    <p>Darren has experienced the most intense highs and lows during both his sporting and business career and his experiences of working through these challenging times inspires others to do so. Darren's relaxed, charismatic style and his positive message resonate with anyone who understands that the road to success is never easy and life frequently throws obstacles in one's way.</p>
  </section>

  <footer class="block rsvp">RSVP information</footer>
  <div class="block phone">
    <svg viewBox="0 0 24 32" aria-hidden="true"><path fill="var(--yellow)" d="M6 1c1.5-.6 2.6.2 3.2 1.6l2 4.6c.5 1.2.1 2.3-.9 3l-2 1.3c.6 3.6 2.4 7.2 5 9.8l2.1-1c1.1-.5 2.300-.2 3 .8l2.8 4c.8 1.2.5 2.5-.7 3.3l-2 1.3C15.5 31.6 11 29 7.5 23.6 3.6 17.6 2.3 11 2.6 6.2 2.7 4 3.8 2 6 1z"/></svg>
    <span>1300 482 716</span>
  </div>

</main>
</body>
</html>
```